CREATE A BUSINESS CARD FOR A BOAT CLEANING SERVICE

WE ARE STARTING A NEW BOAT CLEANING BUSINESS. WE DIVE UNDERWATER TO CLEAN BOAT HULLS, JETTIES, UNDERWATER STRUCTURES ETC. WE ARE LOOKING FOR AN UPPERMARKET MODERN LOGO AND BUSINESS CARD AS ALOT OF OUR TARGET MARKET WILL BE HIGH END. YOU HAVE TO DESIGN A BUSINESS CARD AND LOGO SEPERATELY .
THE BUSINESS CARD DIMESNION MUST BE STANDARD SIZE.
The standard dimensions of a printed business card are 3.5 x 2 inches

Target Market(s)

UNDERWATER SERVICED

Industry/Entity Type

Business

Contact Information for Business Card

HALDEN UNDERWATER SERVICES

Font styles to use
Serif

Colors

Designer to choose colors to be used in the design.

Requirements
Must have
• HALDEN
Nice to have
• dark
Should not have
• more than 3 colors

```html
<!DOCTYPE html>
<html lang="en">
<head>
<meta charset="utf-8">
<title>Halden Underwater Service – Identity</title>
<link rel="stylesheet" href="https://fonts.googleapis.com/css2?family=Saira+Semi+Condensed:wght@400;500;600&family=Open+Sans:wght@400;600;700&display=swap">
<style>
  :root {
    --backdrop: #e4e5e6;
    --navy: #1d2a44;
    --ink: #0f2233;
    --teal: #0a8fb0;
    --teal-deep: #0b3a55;
    --white: #ffffff;
    --shadow: rgba(0, 0, 0, 0.35);
  }
  * { margin: 0; padding: 0; box-sizing: border-box; }
  html, body { width: 1200px; height: 900px; overflow: hidden; }
  body {
    position: relative;
    background: var(--backdrop);
    font-family: "Open Sans", Arial, sans-serif;
  }
  .card {
    position: absolute;
    width: 390px;
    height: 223px;
    box-shadow: 4px 6px 10px var(--shadow);
    overflow: hidden;
  }
  .wordmark {
    font-family: "Saira Semi Condensed", "Arial Narrow", sans-serif;
    text-align: center;
    line-height: 1;
  }
  .wordmark .name { display: block; font-weight: 600; letter-spacing: 0.32em; padding-left: 0.32em; }
  .wordmark .tagline { display: block; font-weight: 400; letter-spacing: 0.2em; padding-left: 0.2em; }
  .mark-dot { display: block; margin: 0 auto; border-radius: 50%; }

  /* Front */
  .card-front {
    left: 310px; top: 238px;
    background: linear-gradient(135deg, var(--teal) 0%, #0a5f80 50%, var(--teal-deep) 100%);
    display: flex; align-items: center; justify-content: center;
  }
  .card-front .mark-dot { width: 34px; height: 34px; background: var(--ink); margin-bottom: 16px; }
  .card-front .name { font-size: 31px; color: var(--ink); }
  .card-front .tagline { font-size: 11px; color: var(--ink); margin-top: 4px; }

  /* Back */
  .card-back { left: 530px; top: 422px; background: var(--navy); }
  .wave-band {
    position: absolute; left: 0; right: 0; top: 140px; bottom: 0;
    background: linear-gradient(160deg, var(--teal) 0%, #0b5f82 60%, var(--teal-deep) 100%);
  }
  .card-back .wordmark { position: absolute; left: 0; right: 0; top: 28px; }
  .card-back .mark-dot { width: 22px; height: 22px; background: var(--white); margin-bottom: 10px; }
  .card-back .name { font-size: 17px; color: var(--white); }
  .card-back .tagline { font-size: 6.5px; color: var(--white); margin-top: 2px; }
  .holder { position: absolute; left: 28px; top: 172px; }
  .holder-name { font-size: 17px; font-weight: 700; color: var(--teal-deep); letter-spacing: 0.01em; }
  .holder-role { font-size: 7px; color: var(--white); margin: 2px 0 0 30px; }
  .contacts { position: absolute; left: 236px; top: 156px; list-style: none; }
  .contacts li { display: flex; align-items: center; gap: 6px; font-size: 8.5px; color: var(--white); line-height: 14px; }
  .contacts svg { width: 8px; height: 8px; fill: var(--white); }

  /* Logo sheet */
  .logo-sheet {
    position: absolute; left: 82px; top: 538px; width: 372px; height: 318px;
    background: radial-gradient(ellipse at 50% 45%, var(--white) 55%, #ececec 100%);
    display: flex; align-items: center; justify-content: center;
  }
  .logo-sheet .mark-dot { width: 60px; height: 60px; background: var(--teal); margin-bottom: 30px; }
  .logo-sheet .name { font-size: 42px; color: var(--navy); }
  .logo-sheet .tagline { font-size: 15px; color: var(--teal); margin-top: 6px; }
</style>
</head>
<body>

  <section class="card card-front" aria-label="Business card front">
    <div class="wordmark">
      <span class="mark-dot"></span>
      <span class="name">HALDEN</span>
      <span class="tagline">UNDERWATER SERVICE</span>
    </div>
  </section>

  <section class="card card-back" aria-label="Business card back">
    <div class="wave-band" role="img" aria-label="Decorative teal wave band across the lower card"></div>
    <div class="wordmark">
      <span class="mark-dot"></span>
      <span class="name">HALDEN</span>
      <span class="tagline">UNDERWATER SERVICE</span>
    </div>
    <div class="holder">
      <p class="holder-name">MARA ELLISON</p>
      <p class="holder-role">General Manager</p>
    </div>
    <ul class="contacts">
      <li><svg viewBox="0 0 10 10"><circle cx="5" cy="5" r="4.5" fill="none" stroke="#fff" stroke-width="1.4"/><circle cx="5" cy="5" r="1.6"/></svg>mara@halden.com</li>
      <li><svg viewBox="0 0 10 10"><path d="M2 0.5 L4 2.5 L3 4 C3.8 5.6 4.6 6.4 6 7 L7.5 6 L9.5 8 L8 9.5 C4 9 1 6 0.5 2 Z"/></svg>011 482 907 315</li>
      <li><svg viewBox="0 0 10 10"><path d="M5 0.5 L9.5 4.5 L8.3 4.5 L8.3 9.5 L1.7 9.5 L1.7 4.5 L0.5 4.5 Z"/></svg>www.halden.com</li>
    </ul>
  </section>

  <section class="logo-sheet" aria-label="Logo">
    <div class="wordmark">
      <span class="mark-dot"></span>
      <span class="name">HALDEN</span>
      <span class="tagline">UNDERWATER SERVICE</span>
    </div>
  </section>

</body>
</html>
```